PebbleLoom screens tidy up

We would like advice on how to better present the following home page and overview pages.

The existing website is functional, but the pages don't appear professionals and pleasing to the eye. We would specifically like feedback on alignment and padding of icons and text to make the screen more appealing and polished.

We are following the willow design system.

1 page

Sans Serif
• IBM Plex, Poppins

```html
<!DOCTYPE html>
<html lang="en">
<head>
<meta charset="utf-8">
<title>PebbleLoom – Home and Campaign Overview</title>
<link href="https://fonts.googleapis.com/css2?family=Roboto:wght@400;500;700&display=swap" rel="stylesheet">
<style>
:root{
  --navy:#1f2340;
  --navy-line:#3a3f5e;
  --orange:#f18d2b;
  --orange-soft:#fde6cf;
  --blue:#1e83ec;
  --ink:#1c1d2b;
  --muted:#6b6f80;
  --card-bg:#ffffff;
  --page:#ffffff;
  --green:#3ee03a;
}
*{box-sizing:border-box;margin:0;padding:0}
html,body{width:1034px;height:1200px;overflow:hidden;background:var(--page)}
body{position:relative;font-family:'Roboto',sans-serif;color:var(--ink)}

.screen{position:absolute;left:101px;width:833px;height:468px;background:#fff;box-shadow:0 0 8px rgba(20,24,60,.08)}
.screen--home{top:98px}
.screen--campaign{top:633px}

.sidebar{position:absolute;left:0;top:0;width:190px;height:468px;background:var(--navy);border-radius:0 23px 23px 0;color:#fff}
.sidebar__menu{position:absolute;left:24px;top:23px}
.sidebar__brand{position:absolute;left:54px;top:18px;display:flex;align-items:center;gap:7px;font-size:12px;font-weight:500;letter-spacing:-.2px}
.sidebar__brand-dot{width:17px;height:17px;border-radius:50%;background:#fff}
.sidebar__gear{position:absolute;left:157px;top:23px}
.sidebar__marker{position:absolute;left:0;width:3px;background:var(--orange);border-radius:0 2px 2px 0}
.nav-item{position:absolute;left:24px;width:143px;display:flex;align-items:center;gap:11px;font-size:8px;height:14px}
.nav-item svg{width:11px;height:11px;flex:none}
.nav-item--active{color:var(--orange)}
.nav-item__plus{margin-left:auto;font-size:9px}
.nav-divider{position:absolute;left:24px;width:143px;height:1px;background:var(--navy-line)}
.campaign-toggle{position:absolute;left:24px;width:143px;height:26px;background:var(--orange);display:flex;align-items:center;padding:0 10px 0 18px;gap:11px;font-size:8px;color:#fff}
.campaign-toggle__caret{margin-left:auto;font-size:6px}
.sub-item{position:absolute;left:42px;font-size:7.5px;color:#fff}
.sub-item--active{color:var(--orange)}

.main{position:absolute;left:227px;top:0;right:0;bottom:0}
.section-title{position:absolute;font-size:11px;font-weight:700;color:var(--ink)}
.btn-add{position:absolute;left:73px;top:225px;width:43px;height:15px;background:var(--navy);color:#fff;font-size:5px;font-weight:700;display:flex;align-items:center;justify-content:center;border-radius:1px}

.card{position:absolute;width:180px;height:135px;background:var(--card-bg);border-radius:6px;box-shadow:0 1px 6px rgba(30,35,70,.10);padding:24px 20px 0}
.card__icon{width:34px;height:34px;border-radius:50%;background:var(--orange);border:2px solid var(--orange-soft);display:flex;align-items:center;justify-content:center}
.card__icon svg{width:16px;height:16px}
.card__title{margin-top:11px;font-size:10px;font-weight:700;color:var(--ink)}
.card__text{margin-top:3px;font-size:7.2px;line-height:13.5px;color:var(--muted)}
.card__stats{margin-top:3px;display:flex;align-items:center;gap:4px;font-size:7.2px;color:var(--muted)}
.card__stats svg{width:8px;height:8px}
.card__stats .gap{width:6px}
.card__signal{position:absolute;left:137px;top:35px}
.card__progress{position:absolute;left:20px;top:110px;width:135px;height:2px;background:#e3e3e8}
.card__progress span{display:block;width:31px;height:2px;background:var(--orange)}
.card__badge{position:absolute;left:122px;top:16px;width:44px;height:15px;background:var(--navy);color:#fff;font-size:5px;font-weight:700;display:flex;align-items:center;justify-content:center;border-radius:1px}

.campaign-card{position:absolute;top:254px;width:180px;height:135px;border-radius:6px;color:#fff;padding:17px 19px 0}
.campaign-card--blue{background:var(--blue)}
.campaign-card--orange{background:var(--orange)}
.campaign-card__icon{width:36px;height:36px;border-radius:50%;background:var(--orange);border:2px solid #fff;display:flex;align-items:center;justify-content:center}
.campaign-card__icon svg{width:16px;height:16px}
.campaign-card__title{margin-top:9px;font-size:10px;font-weight:700}
.campaign-card__text{margin-top:7px;font-size:6.5px}
.campaign-card__meta{position:absolute;left:19px;top:98px;right:10px;display:flex;align-items:center}
.campaign-card__count{font-size:24px;font-weight:500;line-height:1;width:18px}
.campaign-card__label{font-size:5px;line-height:9px}
.campaign-card__since{margin-left:auto;display:flex;align-items:center;gap:5px;font-size:5px;line-height:9px}
.campaign-card__dot{width:6px;height:6px;border-radius:50%;background:var(--green)}
</style>
</head>
<body>

<!-- ===== Home screen ===== -->
<section class="screen screen--home">
  <nav class="sidebar">
    <svg class="sidebar__menu" width="12" height="10" viewBox="0 0 12 10"><rect y="0" width="12" height="1.6" fill="#fff"/><rect y="4" width="9" height="1.6" fill="#fff"/><rect y="8" width="6" height="1.6" fill="#fff"/></svg>
    <div class="sidebar__brand"><span class="sidebar__brand-dot"></span>PebbleLoom</div>
    <svg class="sidebar__gear" width="10" height="10" viewBox="0 0 10 10"><circle cx="5" cy="5" r="3.6" fill="none" stroke="#fff" stroke-width="2.2" stroke-dasharray="1.6 1"/><circle cx="5" cy="5" r="1.1" fill="#fff"/></svg>

    <span class="sidebar__marker" style="top:63px;height:25px"></span>
    <div class="nav-item nav-item--active" style="top:66px"><svg viewBox="0 0 12 12"><path d="M6 1 0.5 6h1.8v5h3v-3h1.4v3h3V6h1.8z" fill="#f18d2b"/></svg>Home</div>
    <span class="nav-divider" style="top:88px"></span>
    <div class="nav-item" style="top:102px"><svg viewBox="0 0 12 12"><path d="M6 1a3.5 3.5 0 0 0-3.5 3.5V8L1.3 9.5h9.4L9.5 8V4.5A3.5 3.5 0 0 0 6 1zm-1.3 9.5a1.3 1.3 0 0 0 2.6 0z" fill="#fff"/></svg>All Alerts</div>
    <span class="nav-divider" style="top:124px"></span>
    <div class="nav-item" style="top:135px"><svg viewBox="0 0 12 12"><circle cx="3" cy="3.5" r="1.5" fill="#fff"/><circle cx="9" cy="3.5" r="1.5" fill="#fff"/><circle cx="6" cy="5.5" r="1.7" fill="#fff"/><path d="M3 8h6v3H3z" fill="#fff"/></svg>Manage</div>
    <span class="nav-divider" style="top:157px"></span>
    <div class="nav-item" style="top:170px"><svg viewBox="0 0 12 12"><path d="M1 7l7-4v6z" fill="#fff"/><rect x="2.5" y="8" width="2" height="3" fill="#fff"/></svg>Campaigns<span class="nav-item__plus">+</span></div>
    <div class="campaign-toggle" style="top:192px"><svg width="10" height="10" viewBox="0 0 10 10"><circle cx="5" cy="5" r="3.6" fill="none" stroke="#fff" stroke-width="2.2" stroke-dasharray="1.6 1"/></svg>My Custom Campaign<span class="campaign-toggle__caret">▲</span></div>
    <div class="sub-item" style="top:232px">Overview</div>
    <div class="sub-item" style="top:247px">Files &amp; HoneyTokens</div>
    <div class="sub-item" style="top:263px">Resources</div>
    <div class="sub-item" style="top:278px">Alerts</div>
    <div class="sub-item" style="top:294px">Settings</div>
    <div class="campaign-toggle" style="top:324px"><svg width="10" height="10" viewBox="0 0 10 10"><circle cx="5" cy="5" r="3.6" fill="none" stroke="#fff" stroke-width="2.2" stroke-dasharray="1.6 1"/></svg>Default Campaign<span class="campaign-toggle__caret">▼</span></div>
    <div class="nav-item" style="top:430px"><svg viewBox="0 0 12 12"><circle cx="6" cy="6" r="5" fill="#fff"/><circle cx="6" cy="4.8" r="1.7" fill="#1f2340"/><path d="M3 9.3a3.3 3.3 0 0 1 6 0" fill="#1f2340"/></svg>Profile</div>
  </nav>

  <div class="main">
    <h1 class="section-title" style="left:0;top:40px">Home</h1>

    <article class="card" style="left:0;top:70px">
      <div class="card__icon"><svg viewBox="0 0 16 16"><circle cx="4" cy="5" r="2" fill="#fff"/><circle cx="12" cy="5" r="2" fill="#fff"/><circle cx="8" cy="4" r="2.4" fill="#fff"/><path d="M1 13v-3a2 2 0 0 1 2-2h2v5zM15 13v-3a2 2 0 0 0-2-2h-2v5zM5 13V9.5A2.5 2.5 0 0 1 7.5 7h1A2.5 2.5 0 0 1 11 9.5V13z" fill="#fff"/></svg></div>
      <h2 class="card__title">TeamSpace</h2>
      <p class="card__text">The default cilent is created as a part of<br>your user account.</p>
    </article>

    <article class="card" style="left:194px;top:70px">
      <div class="card__icon"><svg viewBox="0 0 16 16"><circle cx="8" cy="8" r="6" fill="none" stroke="#fff" stroke-width="1.3" stroke-dasharray="3 1.5"/><circle cx="8" cy="8" r="3.6" fill="#fff"/><text x="8" y="10.2" font-size="5.5" font-weight="700" text-anchor="middle" fill="#f18d2b" font-family="Roboto,sans-serif">$</text></svg></div>
      <h2 class="card__title">Starter Pack Usage</h2>
      <p class="card__text">0 Files active out of 10 allowed.</p>
      <svg class="card__signal" width="18" height="13" viewBox="0 0 18 13"><rect x="0" y="8" width="3" height="5" rx="1.2" fill="#6b6f80"/><rect x="5" y="6" width="3" height="7" rx="1.2" fill="#6b6f80"/><rect x="10" y="3" width="3" height="10" rx="1.2" fill="#6b6f80"/><rect x="15" y="0" width="3" height="13" rx="1.2" fill="#6b6f80"/></svg>
      <div class="card__progress"><span></span></div>
    </article>

    <article class="card" style="left:387px;top:70px">
      <div class="card__icon"><svg viewBox="0 0 16 16"><path d="M2 4h4.5l1.3 1.5H14V13H2z" fill="#fff"/></svg></div>
      <h2 class="card__title">Files &amp; HoneyTokens</h2>
      <p class="card__text">Statistics</p>
      <div class="card__stats"><svg viewBox="0 0 8 8"><circle cx="4" cy="4" r="3.3" fill="none" stroke="#1c1d2b" stroke-width=".8"/><path d="M2.4 4.1l1.1 1.1L5.8 2.8" fill="none" stroke="#1c1d2b" stroke-width=".8"/></svg>0<span class="gap"></span><svg viewBox="0 0 8 8"><path d="M0 1.5h3l.8 1H8V7H0z" fill="#1c1d2b"/></svg>30</div>
    </article>

    <h2 class="section-title" style="left:0;top:226px">Campaigns</h2>
    <div class="btn-add">+ Add New</div>

    <article class="campaign-card campaign-card--blue" style="left:0">
      <div class="campaign-card__icon"><svg viewBox="0 0 16 16"><rect x="3" y="5" width="10" height="9" rx="1" fill="#fff"/><path d="M6 5V3.5a2 2 0 0 1 4 0V5" fill="none" stroke="#fff" stroke-width="1.2"/></svg></div>
      <h2 class="campaign-card__title">My Custom Campaign</h2>
      <p class="campaign-card__text">This is my custom campaign for finding</p>
      <div class="campaign-card__meta"><span class="campaign-card__count">0</span><span class="campaign-card__label">Active<br>Files &amp; HoneyTokens</span><span class="campaign-card__since"><span class="campaign-card__dot"></span><span>Active Since :<br>July 25 2023 13:12</span></span></div>
    </article>

    <article class="campaign-card campaign-card--orange" style="left:194px">
      <div class="campaign-card__icon"><svg viewBox="0 0 16 16"><rect x="3" y="5" width="10" height="9" rx="1" fill="#fff"/><path d="M6 5V3.5a2 2 0 0 1 4 0V5" fill="none" stroke="#fff" stroke-width="1.2"/></svg></div>
      <h2 class="campaign-card__title">Default Campaign</h2>
      <p class="campaign-card__text">Define your own mission, or combaine different</p>
      <div class="campaign-card__meta"><span class="campaign-card__count">0</span><span class="campaign-card__label">Active<br>Files &amp; HoneyTokens</span><span class="campaign-card__since"><span class="campaign-card__dot"></span><span>Active Since :<br>July 25 2023 13:12</span></span></div>
    </article>
  </div>
</section>

<!-- ===== Campaign overview screen ===== -->
<section class="screen screen--campaign">
  <nav class="sidebar">
    <svg class="sidebar__menu" width="12" height="10" viewBox="0 0 12 10"><rect y="0" width="12" height="1.6" fill="#fff"/><rect y="4" width="9" height="1.6" fill="#fff"/><rect y="8" width="6" height="1.6" fill="#fff"/></svg>
    <div class="sidebar__brand"><span class="sidebar__brand-dot"></span>PebbleLoom</div>
    <svg class="sidebar__gear" width="10" height="10" viewBox="0 0 10 10"><circle cx="5" cy="5" r="3.6" fill="none" stroke="#fff" stroke-width="2.2" stroke-dasharray="1.6 1"/><circle cx="5" cy="5" r="1.1" fill="#fff"/></svg>

    <div class="nav-item" style="top:66px"><svg viewBox="0 0 12 12"><path d="M6 1 0.5 6h1.8v5h3v-3h1.4v3h3V6h1.8z" fill="#fff"/></svg>Home</div>
    <span class="nav-divider" style="top:88px"></span>
    <div class="nav-item" style="top:102px"><svg viewBox="0 0 12 12"><path d="M6 1a3.5 3.5 0 0 0-3.5 3.5V8L1.3 9.5h9.4L9.5 8V4.5A3.5 3.5 0 0 0 6 1zm-1.3 9.5a1.3 1.3 0 0 0 2.6 0z" fill="#fff"/></svg>All Alerts</div>
    <span class="nav-divider" style="top:124px"></span>
    <div class="nav-item" style="top:135px"><svg viewBox="0 0 12 12"><circle cx="3" cy="3.5" r="1.5" fill="#fff"/><circle cx="9" cy="3.5" r="1.5" fill="#fff"/><circle cx="6" cy="5.5" r="1.7" fill="#fff"/><path d="M3 8h6v3H3z" fill="#fff"/></svg>Manage</div>
    <span class="nav-divider" style="top:157px"></span>
    <div class="nav-item" style="top:170px"><svg viewBox="0 0 12 12"><path d="M1 7l7-4v6z" fill="#fff"/><rect x="2.5" y="8" width="2" height="3" fill="#fff"/></svg>Campaigns<span class="nav-item__plus">+</span></div>
    <div class="campaign-toggle" style="top:192px"><svg width="10" height="10" viewBox="0 0 10 10"><circle cx="5" cy="5" r="3.6" fill="none" stroke="#fff" stroke-width="2.2" stroke-dasharray="1.6 1"/></svg>My Custom Campaign<span class="campaign-toggle__caret">▲</span></div>
    <span class="sidebar__marker" style="top:229px;height:16px"></span>
    <div class="sub-item sub-item--active" style="top:232px">Overview</div>
    <div class="sub-item" style="top:247px">Files &amp; HoneyTokens</div>
    <div class="sub-item" style="top:263px">Resources</div>
    <div class="sub-item" style="top:278px">Alerts</div>
    <div class="sub-item" style="top:294px">Settings</div>
    <div class="campaign-toggle" style="top:324px"><svg width="10" height="10" viewBox="0 0 10 10"><circle cx="5" cy="5" r="3.6" fill="none" stroke="#fff" stroke-width="2.2" stroke-dasharray="1.6 1"/></svg>Default Campaign<span class="campaign-toggle__caret">▼</span></div>
  </nav>

  <div class="main">
    <h1 class="section-title" style="left:0;top:40px">Campaign</h1>

    <article class="card" style="left:0;top:70px">
      <span class="card__badge">Custom</span>
      <div class="card__icon"><svg viewBox="0 0 16 16"><circle cx="4" cy="5" r="2" fill="#fff"/><circle cx="12" cy="5" r="2" fill="#fff"/><circle cx="8" cy="4" r="2.4" fill="#fff"/><path d="M1 13v-3a2 2 0 0 1 2-2h2v5zM15 13v-3a2 2 0 0 0-2-2h-2v5zM5 13V9.5A2.5 2.5 0 0 1 7.5 7h1A2.5 2.5 0 0 1 11 9.5V13z" fill="#fff"/></svg></div>
      <h2 class="card__title">My Custom Campaign</h2>
      <p class="card__text">This is mu custom campaign for finding i</p>
    </article>

    <article class="card" style="left:195px;top:70px">
      <div class="card__icon"><svg viewBox="0 0 16 16"><circle cx="8" cy="3" r="1.8" fill="#fff"/><path d="M8 5v3M3 11V8h10v3" fill="none" stroke="#fff" stroke-width="1.2"/><circle cx="3" cy="12" r="1.8" fill="#fff"/><circle cx="8" cy="12" r="1.8" fill="#fff"/><circle cx="13" cy="12" r="1.8" fill="#fff"/><path d="M8 8v2" stroke="#fff" stroke-width="1.2"/></svg></div>
      <h2 class="card__title">Campaign Organisation</h2>
      <p class="card__text">Self-enabling Deliverables Proprietary<br>Limited ( Standard )</p>
      <div class="card__stats"><svg viewBox="0 0 8 8"><circle cx="4" cy="1.5" r="1.1" fill="#6b6f80"/><path d="M4 2.6v2M1.5 6V4.6h5V6" fill="none" stroke="#6b6f80" stroke-width=".7"/><circle cx="1.5" cy="6.6" r="1" fill="#6b6f80"/><circle cx="4" cy="6.6" r="1" fill="#6b6f80"/><circle cx="6.5" cy="6.6" r="1" fill="#6b6f80"/></svg><span style="margin-left:3px">80</span></div>
    </article>

    <article class="card" style="left:387px;top:70px">
      <div class="card__icon"><svg viewBox="0 0 16 16"><circle cx="8" cy="3" r="1.8" fill="#fff"/><path d="M8 5v3M3 11V8h10v3" fill="none" stroke="#fff" stroke-width="1.2"/><circle cx="3" cy="12" r="1.8" fill="#fff"/><circle cx="8" cy="12" r="1.8" fill="#fff"/><circle cx="13" cy="12" r="1.8" fill="#fff"/><path d="M8 8v2" stroke="#fff" stroke-width="1.2"/></svg></div>
      <h2 class="card__title">Campaign Organisation</h2>
      <p class="card__text">Unleash Bleeding-edge mindshare<br>8 Hours ago</p>
      <div class="card__stats"><svg viewBox="0 0 8 8"><circle cx="4" cy="1.5" r="1.1" fill="#6b6f80"/><path d="M4 2.6v2M1.5 6V4.6h5V6" fill="none" stroke="#6b6f80" stroke-width=".7"/><circle cx="1.5" cy="6.6" r="1" fill="#6b6f80"/><circle cx="4" cy="6.6" r="1" fill="#6b6f80"/><circle cx="6.5" cy="6.6" r="1" fill="#6b6f80"/></svg><span style="margin-left:3px">8</span></div>
    </article>

    <article class="card" style="left:0;top:226px;padding-top:20px">
      <div class="card__icon"><svg viewBox="0 0 16 16"><path d="M2 4h4.5l1.3 1.5H14V13H2z" fill="#fff"/></svg></div>
      <h2 class="card__title">Files &amp; HoneyTokens</h2>
      <p class="card__text">Statistics</p>
      <div class="card__stats"><svg viewBox="0 0 8 8"><circle cx="4" cy="4" r="3.3" fill="none" stroke="#1c1d2b" stroke-width=".8"/><path d="M2.4 4.1l1.1 1.1L5.8 2.8" fill="none" stroke="#1c1d2b" stroke-width=".8"/></svg>0<span class="gap"></span><svg viewBox="0 0 8 8"><path d="M0 1.5h3l.8 1H8V7H0z" fill="#1c1d2b"/></svg>30</div>
    </article>

    <article class="card" style="left:194px;top:226px;padding-top:20px">
      <div class="card__icon"><svg viewBox="0 0 16 16"><circle cx="5.5" cy="6" r="2.6" fill="none" stroke="#fff" stroke-width="1.1"/><circle cx="11" cy="6" r="2" fill="none" stroke="#fff" stroke-width="1.1"/><circle cx="8.5" cy="2.6" r="1.4" fill="none" stroke="#fff" stroke-width="1"/><path d="M1.5 11.5h4l3 1 5-2v2l-5 2.2-3-1h-4z" fill="#fff"/></svg></div>
      <h2 class="card__title">Resources</h2>
      <p class="card__text">Generate a collection of fictional<br>organisations, custome templates, Uploaded<br>files &amp; logos</p>
    </article>

    <article class="card" style="left:387px;top:226px;padding-top:20px">
      <div class="card__icon"><svg viewBox="0 0 16 16"><path d="M8 2 15 14H1z" fill="#fff"/><rect x="7.3" y="6" width="1.4" height="4.5" fill="#f18d2b"/><rect x="7.3" y="11.3" width="1.4" height="1.4" fill="#f18d2b"/></svg></div>
      <h2 class="card__title">Alerts</h2>
      <p class="card__text">Alert statistics will appear here</p>
    </article>
  </div>
</section>

</body>
</html>
```